Wow me with your Earring card options!

An A7 portrait sized earring card is required for Velvet & Vinyl. Inspired by Velvet and fueled by Vinyl we love our accessories to do the talking. Bold statement earrings are our thing. Our earring cards need to showcase our brand while not stealing all of the limelight from the earrings themselves. Earring care information needs to be included on the back side of the card. Our simple logo needs to be the basis for the colour choices used on the card.

Need extra days to review

• No florals please 😊

```html
<!DOCTYPE html>
<html lang="en">
<head>
<meta charset="utf-8">
<title>Velvet &amp; Vinyl – Earring Card</title>
<link rel="stylesheet" href="https://fonts.googleapis.com/css2?family=Archivo+Black&family=Caveat:wght@400&family=Roboto+Condensed:ital,wght@1,300;1,400&display=swap">
<style>
  :root {
    --bg: #dcdcdc;
    --ink: #0c0c0e;
    --paper: #ffffff;
    --grey-text: #5a5a5a;
    --heading: #1a1a1a;
    --teal: #4f9fa6;
    --green: #8cc152;
    --orange: #e0692a;
    --pink: #d33f8e;
  }
  * { box-sizing: border-box; margin: 0; padding: 0; }
  html, body { width: 1200px; height: 1200px; overflow: hidden; background: var(--bg); }
  .stage { position: relative; width: 1200px; height: 1200px; }

  .card {
    position: absolute;
    width: 434px;
    height: 616px;
    box-shadow: 0 3px 8px rgba(0,0,0,0.25);
    overflow: hidden;
  }
  .card--front { left: 110px; top: 292px; background: var(--ink); }
  .card--back { left: 628px; top: 290px; background: var(--paper); }

  /* Front */
  .front__rule {
    position: absolute; left: 59px; width: 321px; height: 1px;
    background: #6a6a6a;
  }
  .front__rule--top { top: 57px; }
  .front__rule--bottom { top: 226px; }
  .front__logo-panel {
    position: absolute; left: 45px; top: 64px; width: 349px; height: 149px;
    background: #050506;
    display: flex; align-items: center; justify-content: center;
  }
  .brand-name {
    font-family: "Archivo Black", sans-serif;
    font-size: 40px;
    color: var(--paper);
    letter-spacing: 0.5px;
  }
  .front__ornament {
    position: absolute; left: 0; top: 264px; width: 434px; height: 276px;
    background: radial-gradient(ellipse at 60% 45%, #4a4a4c 0%, #262628 45%, var(--ink) 75%);
  }

  /* Back */
  .care-title {
    position: absolute; left: 0; top: 28px; width: 434px; text-align: center;
    padding-left: 10px;
    font-family: "Roboto Condensed", sans-serif;
    font-style: italic; font-weight: 400;
    font-size: 50px; line-height: 1; letter-spacing: 3px;
    color: var(--heading);
  }
  .care-subtitle {
    position: absolute; left: 117px; top: 72px;
    font-family: "Caveat", cursive;
    font-size: 42px; color: #a8a8a8;
    transform: rotate(-4deg); transform-origin: left center;
  }
  .back__ornament {
    position: absolute; left: 0; top: 300px; width: 434px; height: 240px;
    background: radial-gradient(ellipse at 60% 45%, #d6d6d6 0%, #ececec 45%, var(--paper) 75%);
  }
  .care-item {
    position: absolute; width: 200px; text-align: center;
    font-family: "Roboto Condensed", sans-serif; font-style: italic; font-weight: 400;
    font-size: 19.5px; line-height: 19px; color: var(--grey-text);
  }
  .care-item svg { display: block; margin: 0 auto 6px; }
  .care-item--moisture { left: 22px; top: 138px; }
  .care-item--bed { left: 226px; top: 140px; }
  .care-item--perfume { left: 22px; top: 226px; }
  .care-item--sun { left: 226px; top: 228px; }

  .contact {
    position: absolute; left: 28px; top: 496px; width: 276px;
    border-bottom: 2px solid #b5b5b5; padding-bottom: 2px;
    list-style: none;
  }
  .contact li {
    display: flex; align-items: center; height: 27.5px;
    font-family: "Roboto Condensed", sans-serif; font-style: italic; font-weight: 400;
    font-size: 19px; color: var(--grey-text);
  }
  .contact svg { width: 24px; height: 22px; margin-right: 9px; flex: none; }
  .social {
    position: absolute; left: 306px; top: 573px; width: 112px;
    font-family: "Roboto Condensed", sans-serif; font-style: italic; font-weight: 400;
    font-size: 10px; color: var(--grey-text); text-align: right; line-height: 13px;
  }
</style>
</head>
<body>
<main class="stage">

  <section class="card card--front" aria-label="Card front">
    <div class="front__rule front__rule--top"></div>
    <div class="front__logo-panel">
      <span class="brand-name">Velvet &amp; Vinyl</span>
    </div>
    <div class="front__rule front__rule--bottom"></div>
    <div class="front__ornament" role="img" aria-label="Silver swirling vine ornament with leaves"></div>
  </section>

  <section class="card card--back" aria-label="Card back">
    <div class="back__ornament" role="img" aria-label="Faint grey swirling vine ornament with leaves"></div>
    <h1 class="care-title">EARRING</h1>
    <p class="care-subtitle">Care instructions</p>

    <div class="care-item care-item--moisture">
      <svg width="40" height="38" viewBox="0 0 40 38" fill="none" stroke="var(--teal)" stroke-width="1.6">
        <path d="M13 10 C7 19 4 24 4 28 a9 9 0 0 0 18 0 C22 24 19 19 13 10 Z"/>
        <path d="M27 2 C23 9 21 13 21 16 a6.5 6.5 0 0 0 13 0 C34 13 31 9 27 2 Z"/>
        <path d="M8 27 a5 5 0 0 0 4 6"/>
      </svg>
      Avoid moisture &amp;<br>remove before bathing
    </div>

    <div class="care-item care-item--bed">
      <svg width="44" height="36" viewBox="0 0 44 36" fill="none" stroke="var(--green)" stroke-width="2">
        <rect x="4" y="2" width="36" height="16" rx="3"/>
        <rect x="9" y="9" width="11" height="6" rx="2"/>
        <rect x="24" y="9" width="11" height="6" rx="2"/>
        <rect x="2" y="18" width="40" height="12" rx="2"/>
        <path d="M2 24 H42 M5 30 V34 M39 30 V34"/>
      </svg>
      For comforts sake,<br>remove before bed!
    </div>

    <div class="care-item care-item--perfume">
      <svg width="40" height="40" viewBox="0 0 40 40" fill="none" stroke="var(--orange)" stroke-width="1.6">
        <rect x="14" y="2" width="8" height="6"/>
        <path d="M16 8 V12 M20 8 V12"/>
        <path d="M24 4 L30 1 M24 5 H31 M24 6 L30 9"/>
        <path d="M12 12 H24 C32 15 35 21 34 28 C33 34 28 38 18 38 C8 38 3 34 2 28 C1 21 4 15 12 12 Z"/>
        <path d="M6 28 C12 24 18 32 30 26 C30 32 26 35 18 35 C11 35 7 32 6 28 Z"/>
      </svg>
      Avoid contact with<br>perfumes &amp; lotions
    </div>

    <div class="care-item care-item--sun">
      <svg width="40" height="40" viewBox="0 0 40 40" fill="none" stroke="var(--pink)" stroke-width="1.6">
        <circle cx="20" cy="20" r="9"/>
        <path d="M20 2 V6 M20 34 V38 M2 20 H6 M34 20 H38 M7 7 L10 10 M30 30 L33 33 M33 7 L30 10 M10 30 L7 33 M12 4 L13 7 M28 4 L27 7 M12 36 L13 33 M28 36 L27 33 M4 12 L7 13 M36 12 L33 13 M4 28 L7 27 M36 28 L33 27"/>
        <path d="M15 18 a5 5 0 0 1 4 -4"/>
      </svg>
      Store away from<br>direct sunlight
    </div>

    <ul class="contact">
      <li>
        <svg viewBox="0 0 24 22" fill="none" stroke="#222" stroke-width="1.5">
          <circle cx="12" cy="6" r="4.5"/>
          <path d="M3 21 V17 C3 13 7 12 12 12 C17 12 21 13 21 17 V21 Z"/>
        </svg>
        @velvetandvinyl
      </li>
      <li>
        <svg viewBox="0 0 24 22" fill="none" stroke="#111" stroke-width="1.6">
          <rect x="1.5" y="4" width="21" height="14" fill="#111"/>
          <path d="M2 4.5 L12 12 L22 4.5 M2 17.5 L9 10 M22 17.5 L15 10" stroke="#fff"/>
        </svg>
        hello@velvetandvinyl.com.au
      </li>
      <li>
        <svg viewBox="0 0 24 22" fill="none" stroke="#222" stroke-width="1.4">
          <circle cx="12" cy="11" r="10"/>
          <ellipse cx="12" cy="11" rx="4.5" ry="10"/>
          <path d="M2 11 H22 M4 5.5 H20 M4 16.5 H20 M12 1 V21"/>
        </svg>
        www.velvetandvinyl.com.au
      </li>
    </ul>

    <p class="social">Reelo · Boardo<br>Circlo · Framo</p>
  </section>

</main>
</body>
</html>
```